Graphic Design/Logo Needed for Ear Drops Bottle

We have an Ear Drop Medication that we need to create a new label for. We will use a retro picture of a Doctor (Dr. Blenham) and the name of the product is Tidy Lobe. There is no official logo, so we will want to create a retro, basic logo for Tidy Lobe and use the retro picture. Front portion of the label is Size is 1.5" in height, and about 1.375" Width. this is a small tube similar in size to eye drops. We will be looking for just the logo portion and what you will see on the front of the bottle.

Target Market(s)

Medical Container

Industry/Entity Type

Medical

Font styles to use
Serif
Sans Serif

Colors
0054AA
0677BA
7BADD7
CADEEF
E8F1F8
FFF300
FFF600
FEFA6F
FFFEC7
FFFEE8

Requirements
Must have
• Picture of Dr. Blenham, "Tidy Lobe", Dr. Blenham's Ear Solution
Nice to have
• Retro Style or Modern with Retro Feel, Clean and engaging

```html
<!DOCTYPE html>
<html lang="en">
<head>
<meta charset="utf-8">
<title>Tidy Lobe – Ear Drop Label</title>
<link href="https://fonts.googleapis.com/css2?family=Saira+Extra+Condensed:wght@500;600&display=swap" rel="stylesheet">
<style>
  :root {
    --navy: #0d3f75;
    --sky: #cadeef;
    --sky-line: #b9d2ea;
    --white: #ffffff;
    --yellow: #f2e81e;
    --backdrop: #ffffff;
  }
  * { margin: 0; padding: 0; box-sizing: border-box; }
  html, body {
    width: 1200px; height: 773px; overflow: hidden;
    background: var(--backdrop);
    font-family: "Saira Extra Condensed", "Arial Narrow", sans-serif;
    font-stretch: condensed;
    color: var(--navy);
  }
  .canvas { position: relative; width: 1200px; height: 773px; }
  .label {
    position: absolute; left: 300px; top: 60px;
    width: 600px; height: 652px;
    background: var(--white);
    border: 1px solid var(--sky-line);
    overflow: hidden;
  }
  .label__top-band {
    position: absolute; left: 0; top: 0; width: 100%; height: 35px;
    background: var(--sky);
  }
  .label__main-band {
    position: absolute; left: 0; top: 48px; width: 100%; height: 444px;
    background: var(--sky);
  }
  .doctor-portrait {
    position: absolute; left: 126px; top: 83px; width: 354px; height: 270px;
    border-radius: 140px 140px 0 0;
    background: linear-gradient(180deg, #0d3f75 0%, #2e5f96 70%, #6f97c2 100%);
  }
  .subtitle-tab {
    position: absolute; left: 50%; top: 462px;
    transform: translateX(-50%);
    padding: 10px 34px 16px;
    background: var(--white);
    border-radius: 34px 34px 0 0;
    white-space: nowrap;
    z-index: 1;
  }
  .subtitle {
    font-weight: 500; font-size: 34px; line-height: 1;
    letter-spacing: -0.5px;
  }
  .product-name {
    position: absolute; left: 0; width: 100%; top: 345px;
    text-align: center; white-space: nowrap;
    font-weight: 600; font-size: 120px; line-height: 1;
    letter-spacing: -1px;
    z-index: 2;
  }
  .net-weight {
    position: absolute; left: 1px; right: 1px; top: 580px; height: 54px;
    display: flex; align-items: center; gap: 14px;
    white-space: nowrap;
  }
  .net-weight__rule { flex: 1 1 auto; height: 7px; background: var(--yellow); }
  .net-weight__text { flex: 0 0 auto; font-weight: 500; font-size: 24px; line-height: 1; }
  .net-weight__badge {
    flex: 0 0 auto;
    width: 54px; height: 54px;
    border-radius: 50%; background: var(--navy); color: var(--white);
    display: flex; align-items: center; justify-content: center;
    font-weight: 500; font-size: 24px; line-height: 1; white-space: nowrap;
    margin: 0 -6px;
  }
</style>
</head>
<body>
<main class="canvas">
  <section class="label">
    <div class="label__top-band"></div>
    <div class="label__main-band"></div>
    <div class="doctor-portrait" role="img" aria-label="Retro navy illustration of Dr. Blenham wearing a head mirror, smiling, in a white coat and tie"></div>
    <div class="subtitle-tab"><p class="subtitle">Dr. Blenham's Ear Solution</p></div>
    <h1 class="product-name">Tidy Lobe</h1>
    <div class="net-weight">
      <div class="net-weight__rule"></div>
      <span class="net-weight__text">Nt. Wt.</span>
      <span class="net-weight__badge">2 oz</span>
      <span class="net-weight__text">59 ml</span>
      <div class="net-weight__rule"></div>
    </div>
  </section>
</main>
</body>
</html>
```